Marcus Lindqvist Photography needs a business card designs

I am looking for a business card with a logo clean and simple which I can use that logo on my website or on my pictures. It has to be very classy and very professional. Please look at my website at www.marcuslvqphoto.com for my signature. I'm thinking of something like that for my signature/logo. I'm still working on my website but you get an idea. I'm open to any design but not too busy graphics.

I will be printing the business card from qrivel.com.

Surprise me :)

contact me if you have any questions.

-ML

I'm receiving a lot of black background at the moment. I know my website is all black doesn't mean I want my card to be all black. Please send in with some white background as well. Thanks :)

check out some business cards that I found online. I think they are simple and look really awesome. I don't want a card that is too busy.

http://www.marcuslvqphoto.com/p270092084

Reason: Please extend the date for me. I haven't really receive any good design yet.

Printing

• -a logo that related to my first and last initial of my name "ML"
-double sided
• -I don't want my background to be all black.
-no pictures on the card

```html
<!DOCTYPE html>
<html lang="en">
<head>
<meta charset="utf-8">
<title>Marcus Lindqvist Photography — Business Card</title>
<link rel="stylesheet" href="https://fonts.googleapis.com/css2?family=Jost:wght@400;500&display=swap">
<style>
  :root {
    --backdrop: #818380;
    --card-white: #ffffff;
    --band-black: #0b0b0b;
    --ink: #111111;
    --accent-red: #a3191d;
    --font-main: "Jost", "Futura", sans-serif;
  }
  * { margin: 0; padding: 0; box-sizing: border-box; }
  html, body {
    width: 1200px;
    height: 900px;
    overflow: hidden;
    background: var(--backdrop);
    font-family: var(--font-main);
  }
  .canvas {
    position: relative;
    width: 1200px;
    height: 900px;
  }
  .card {
    position: absolute;
    background: var(--card-white);
    overflow: hidden;
  }
  .card-front { left: 91px; top: 153px; width: 491px; height: 305px; }
  .card-back  { left: 612px; top: 151px; width: 493px; height: 307px; }

  .card-band {
    position: absolute;
    left: 0; right: 0; bottom: 0;
    height: 60px;
    background: var(--band-black);
  }

  .monogram {
    position: absolute;
    color: var(--accent-red);
    font-weight: 400;
    line-height: 1;
    letter-spacing: -1px;
    z-index: 2;
  }
  .card-front .monogram { left: 30px; top: 26px; font-size: 56px; }
  .card-back .monogram  { left: 20px; top: 205px; font-size: 76px; }

  .contact-list {
    position: absolute;
    right: 30px;
    top: 30px;
    list-style: none;
    text-align: right;
    font-size: 19.5px;
    line-height: 27.5px;
    color: var(--ink);
  }
  .contact-label { color: var(--accent-red); margin-right: 4px; }

  .line {
    position: absolute;
    white-space: nowrap;
    text-align: right;
    z-index: 1;
  }

  .identity-name {
    right: 31px;
    top: 222px;
    font-size: 26px;
    line-height: 26px;
    text-transform: uppercase;
    color: var(--ink);
  }
  .identity-role {
    right: 31px;
    top: 249px;
    font-size: 20px;
    line-height: 20px;
    color: var(--accent-red);
  }

  .studio-name {
    right: 23px;
    top: 231px;
    font-size: 18px;
    line-height: 18px;
    text-transform: uppercase;
    color: var(--ink);
  }
  .studio-url {
    right: 23px;
    top: 255px;
    font-size: 20px;
    line-height: 20px;
    color: var(--accent-red);
  }
</style>
</head>
<body>
<main class="canvas">
  <section class="card card-front" aria-label="Card front">
    <div class="monogram">ML</div>
    <ul class="contact-list">
      <li><span class="contact-label">[p]</span>1234.567.890</li>
      <li><span class="contact-label">[e]</span>marcuslindqvist@email.com</li>
      <li><span class="contact-label">[w]</span>www.marcuslvqphoto.com</li>
    </ul>
    <div class="card-band"></div>
    <span class="line identity-name">Marcus Lindqvist</span>
    <span class="line identity-role">Photographer</span>
  </section>

  <section class="card card-back" aria-label="Card back">
    <div class="card-band"></div>
    <div class="monogram">ML</div>
    <span class="line studio-name">Marcus Lindqvist Photography</span>
    <span class="line studio-url">www.marcuslvqphoto.com</span>
  </section>
</main>
</body>
</html>
```